Modern Business Card for Lanternfield 2018

Our company assumes the best about people. We are creating an online community of entrepreneurs and business leaders who struggle with marketing their business online.

This business card should POP! We recently got a new logo and are launching a new website next month, so our business cards should make a statement that feels:
-Fresh
-Smart
-Trustworthy
-Fun

Target Market(s)

small business owners, entrepreneurs

Industry/Entity Type

Digital Marketing

Contact Information for Business Card

Dimensions: 3.5" x 2"

Font styles to use
Sans Serif

Colors
f37122
ffffff

Requirements
Must have
• We need a business card with a modern, bold design. We will use one side of the card as a lead-generation offer, so text on one side will need to fit up to 140 characters. The business card should stick to our core colors (orange, black, and white).
Nice to have
• We think a vertical "portrait" design could be interesting.
Should not have
• Should not look like a traditional business card. The round icon should stand out from a distance.

```html
<!DOCTYPE html>
<html lang="en">
<head>
<meta charset="utf-8">
<title>Story Making Coach – Dana Whitlow</title>
<link rel="stylesheet" href="https://fonts.googleapis.com/css2?family=Inter:wght@700&family=Montserrat:wght@600&family=Yellowtail&display=swap">
<style>
  :root {
    --brand-orange: #f37122;
    --cream: #f4f2e6;
    --ink: #1b1b1b;
    --paper-light: #e9dcc6;
    --paper-mid: #cdb89a;
    --paper-dark: #8e735a;
  }
  * { margin: 0; padding: 0; box-sizing: border-box; }
  html, body { width: 1200px; height: 1006px; overflow: hidden; background: var(--cream); }
  .card { position: relative; width: 1200px; height: 1006px; overflow: hidden; }

  .hero {
    position: absolute; left: 0; top: 0; width: 1200px; height: 329px;
    background:
      radial-gradient(ellipse at 30% 40%, rgba(255,255,255,0.35), transparent 60%),
      linear-gradient(135deg, var(--paper-light) 0%, var(--paper-mid) 55%, var(--paper-dark) 100%);
  }
  .headline {
    position: absolute; left: 0; top: 14px; width: 1200px; text-align: center;
    font-family: "Inter", Arial, sans-serif; font-weight: 700;
    font-size: 90px; letter-spacing: -1px; line-height: 1.1; color: var(--ink);
  }

  .name-band {
    position: absolute; left: 0; top: 329px; width: 1200px; height: 348px;
    background: var(--brand-orange);
  }
  .person-name {
    position: absolute; left: 0; top: 78px; width: 1200px; text-align: center;
    font-family: "Yellowtail", cursive; font-size: 112px; line-height: 1.2;
    color: var(--cream);
  }
  .email {
    position: absolute; left: 0; top: 268px; width: 1200px; text-align: center;
    font-family: "Montserrat", Arial, sans-serif; font-weight: 600;
    font-size: 29px; letter-spacing: 4px; color: var(--cream);
  }

  .brand-zone {
    position: absolute; left: 0; top: 677px; width: 1200px; height: 329px;
    background: var(--cream);
    display: flex; align-items: center; justify-content: center; gap: 28px;
  }
  .brand-dot { width: 120px; height: 120px; border-radius: 50%; background: var(--brand-orange); }
  .brand-name {
    font-family: "Inter", Arial, sans-serif; font-weight: 700;
    font-size: 72px; color: var(--brand-orange);
  }
</style>
</head>
<body>
  <main class="card">
    <section class="hero" role="img" aria-label="Photograph of many open books laid flat side by side"></section>
    <h1 class="headline">Story Making Coach</h1>

    <section class="name-band">
      <p class="person-name">Dana Whitlow</p>
      <p class="email">DANA@LANTERNFIELDNOW.COM</p>
    </section>

    <section class="brand-zone">
      <span class="brand-dot"></span>
      <span class="brand-name">Lanternfield</span>
    </section>
  </main>
</body>
</html>
```